Custom Truck shop New Business Card design

double sided business card including my new logo, brand colors and picking a font I attached, clean and modern look. I attached the old card for some reference. and would like to include the picture of the white truck attached. I would also like to have it with one of my employees info as well. (same info except name and title Brin Tolvay Service Writer)

Dale Porvick
Owner

address
48310 E Calloway Ridge Rd S
STE 217
Marsh Hollow, CO 80219

phone 720-555-0184

email dale@brokenspurrigs.example

website brokenspurrgis.example

social @brokenspurrigs

Target Market(s)

men 18-60

Industry/Entity Type

Automotive

Contact Information for Business Card

Dale Porvick Owner address 48310 E Calloway Ridge Rd S STE 217 Marsh Hollow, CO 80219 phone 720-555-0184 email dale@brokenspurrigs.example website brokenspurrgis.example social @brokenspurrigs

Font styles to use
Other font styles liked:
• fonts attached

Requirements
Must have
• new logo, orange #FC68D, Charcoal #333333
Nice to have
• the white truck

```html
<!DOCTYPE html>
<html lang="en">
<head>
<meta charset="utf-8">
<title>Broken Spur Rigs – Business Card</title>
<link href="https://fonts.googleapis.com/css2?family=Jost:wght@400;500;600;700&display=swap" rel="stylesheet">
<style>
  :root {
    --orange: #f26a2e;
    --charcoal: #333333;
    --card-dark: #2b2b2c;
    --backdrop: #3a3d40;
    --white: #f2f2f2;
    --grey-text: #cfcfcf;
  }
  * { margin: 0; padding: 0; box-sizing: border-box; }
  html, body { width: 1200px; height: 952px; overflow: hidden; }
  body {
    background: var(--backdrop);
    font-family: "Jost", "Futura", sans-serif;
    position: relative;
  }
  .card {
    position: absolute;
    left: 320px;
    width: 560px;
    height: 320px;
    border-radius: 20px;
    background: var(--card-dark);
    overflow: hidden;
    box-shadow: 0 14px 30px rgba(0,0,0,0.35);
  }
  .card--front { top: 70px; }
  .card--back { top: 540px; }

  /* Front face */
  .brand-mark {
    position: absolute;
    left: 50%;
    top: 30px;
    width: 72px;
    height: 72px;
    margin-left: -36px;
    border: 3px solid var(--orange);
    border-radius: 50%;
  }
  .brand-name {
    position: absolute;
    left: 0; right: 0;
    top: 116px;
    text-align: center;
    color: var(--orange);
    font-weight: 600;
    font-size: 40px;
    letter-spacing: 1px;
    line-height: 1;
  }
  .brand-sub {
    position: absolute;
    left: 0; right: 0;
    top: 166px;
    display: flex;
    justify-content: center;
    align-items: center;
    gap: 14px;
    color: var(--orange);
    font-weight: 600;
    font-size: 13px;
    letter-spacing: 6px;
  }
  .brand-sub__rule { width: 110px; height: 1.5px; background: var(--orange); }
  .social {
    position: absolute;
    left: 0; right: 0;
    top: 206px;
    text-align: center;
    color: var(--orange);
    font-size: 17px;
    letter-spacing: 2px;
  }
  .front-band {
    position: absolute;
    left: 0; right: 0;
    top: 252px;
    height: 26px;
    background: var(--orange);
  }

  /* Back face */
  .truck-photo {
    position: absolute;
    left: 0; top: 0;
    width: 560px;
    height: 150px;
    background: linear-gradient(180deg, #5d6b5a 0%, #a9adb0 45%, #e4e6e8 70%, #8a8d90 100%);
  }
  .photo-rule {
    position: absolute;
    left: 0; right: 0;
    top: 150px;
    height: 4px;
    background: var(--orange);
  }
  .person {
    position: absolute;
    left: 32px;
    top: 172px;
  }
  .person__name {
    font-size: 26px;
    font-weight: 500;
    color: var(--white);
    line-height: 1;
    letter-spacing: 0.5px;
  }
  .person__name span { color: var(--orange); font-weight: 600; }
  .person__title {
    margin-top: 6px;
    font-size: 17px;
    color: var(--grey-text);
  }
  .contacts {
    position: absolute;
    left: 296px;
    top: 166px;
    list-style: none;
  }
  .contacts li {
    display: flex;
    align-items: center;
    gap: 9px;
    font-size: 14px;
    color: var(--white);
    height: 24px;
  }
  .contacts svg { width: 16px; height: 16px; flex: none; }
  .address-band {
    position: absolute;
    left: 0; right: 0;
    top: 258px;
    height: 30px;
    background: var(--orange);
    color: var(--charcoal);
    font-weight: 700;
    font-size: 14px;
    line-height: 30px;
    padding-left: 32px;
  }
</style>
</head>
<body>

<section class="card card--front">
  <div class="brand-mark"></div>
  <div class="brand-name">BROKEN SPUR</div>
  <div class="brand-sub">
    <span class="brand-sub__rule"></span>
    <span>RIGS</span>
    <span class="brand-sub__rule"></span>
  </div>
  <div class="social">social @brokenspurrigs</div>
  <div class="front-band"></div>
</section>

<section class="card card--back">
  <div class="truck-photo" role="img" aria-label="Photo of a lifted white pickup truck parked outdoors"></div>
  <div class="photo-rule"></div>

  <div class="person">
    <div class="person__name">DALE <span>PORVICK</span></div>
    <div class="person__title">Owner</div>
  </div>

  <ul class="contacts">
    <li>
      <svg viewBox="0 0 16 16"><rect width="16" height="16" rx="3" fill="#f2f2f2"/><path d="M5 3.5l2 2.2-1 1.3c.7 1.4 1.6 2.3 3 3l1.3-1 2.2 2-1 1.6c-3.8-.4-6.8-3.4-7.2-7.2z" fill="#2b2b2c"/></svg>
      720-555-0184
    </li>
    <li>
      <svg viewBox="0 0 16 16"><rect width="16" height="16" rx="3" fill="#f2f2f2"/><rect x="3" y="4.5" width="10" height="7" fill="none" stroke="#2b2b2c" stroke-width="1.3"/><path d="M3 4.5l5 4 5-4" fill="none" stroke="#2b2b2c" stroke-width="1.3"/></svg>
      dale@brokenspurrigs.example
    </li>
    <li>
      <svg viewBox="0 0 16 16"><rect width="16" height="16" rx="3" fill="#f2f2f2"/><circle cx="8" cy="8" r="4.5" fill="none" stroke="#2b2b2c" stroke-width="1.3"/><path d="M3.5 8h9M8 3.5c-2 2.5-2 6.5 0 9M8 3.5c2 2.5 2 6.5 0 9" fill="none" stroke="#2b2b2c" stroke-width="1"/></svg>
      brokenspurrgis.example
    </li>
  </ul>

  <div class="address-band">48310 E Calloway Ridge Rd S STE 217 Marsh Hollow, CO 80219</div>
</section>

</body>
</html>
```